Quillrests.com website overhaul

We want to upgrade our Wix website into a professional looking page for our growing business. The content that is online now needs to be used but the site should have a new look and feel from top to bottom. QuillRests is a company in the hospital and nursing home space. We would like to see the website use our color scheme but other than that we are open to any and all ideas. www.quillrests.com

```html
<!DOCTYPE html>
<html lang="en">
<head>
<meta charset="utf-8">
<title>QuillRests – Contact</title>
<link href="https://fonts.googleapis.com/css2?family=Montserrat:wght@300;600;700&family=DM+Sans:wght@400;500;700&display=swap" rel="stylesheet">
<style>
  :root {
    --ink: #22113f;
    --navy: #3d4c98;
    --hero-dark: #1c0c3c;
    --hero-light: #2c3380;
    --orange: #f65a3b;
    --white: #ffffff;
    --muted: #4a4560;
    --field-text: #3b3553;
  }
  * { margin: 0; padding: 0; box-sizing: border-box; }
  html, body { width: 1002px; height: 1200px; overflow: hidden; background: var(--white); }
  body { position: relative; font-family: "DM Sans", sans-serif; color: var(--ink); }
  .abs { position: absolute; }

  /* header */
  .site-header { position: absolute; left: 0; top: 0; width: 1002px; height: 68px; background: var(--white); }
  .brand { position: absolute; display: flex; align-items: center; gap: 10px; font-family: "Montserrat", sans-serif; font-weight: 700; }
  .brand-dot { width: 26px; height: 26px; border-radius: 50%; background: var(--navy); }
  .site-header .brand { left: 90px; top: 14px; font-size: 30px; color: var(--ink); line-height: 40px; }
  .main-nav a { position: absolute; top: 23px; font-size: 13px; font-weight: 500; color: var(--ink); text-decoration: none; }
  .main-nav a.active::after { content: ""; position: absolute; left: 1px; right: -6px; bottom: -7px; height: 1px; background: var(--navy); }
  .call { position: absolute; display: flex; align-items: center; gap: 6px; font-weight: 500; }
  .call-icon { width: 25px; height: 25px; border-radius: 50%; background: var(--orange); display: flex; align-items: center; justify-content: center; }
  .site-header .call { left: 788px; top: 21px; font-size: 13.5px; color: var(--ink); }

  /* hero */
  .hero { position: absolute; left: 0; top: 68px; width: 1002px; height: 411px; overflow: hidden;
    background: linear-gradient(160deg, var(--hero-dark) 0%, #241752 50%, var(--hero-light) 100%); }
  .hero-kicker { position: absolute; left: 90px; top: 154px; font-size: 22px; color: var(--white); font-weight: 400; }
  .hero-title { position: absolute; left: 89px; top: 178px; font-family: "Montserrat", sans-serif; font-weight: 700; font-size: 42px; color: var(--white); }
  .hero-art { position: absolute; left: 0; top: 0; }

  /* contact section */
  .contact-heading { position: absolute; left: 103px; top: 570px; font-family: "Montserrat", sans-serif; color: var(--ink); }
  .contact-heading .light { display: block; font-weight: 300; font-size: 32px; line-height: 38px; }
  .contact-heading .bold { display: block; font-weight: 700; font-size: 32px; line-height: 40px; }
  .heading-rule { position: absolute; left: 105px; top: 652px; width: 47px; height: 2px; background: var(--navy); }
  .intro { position: absolute; left: 105px; top: 673px; width: 340px; font-size: 13.5px; line-height: 23px; color: var(--muted); }
  .info-badge { position: absolute; width: 70px; height: 70px; border-radius: 50%; border: 2px solid #d7d5e6; display: flex; align-items: center; justify-content: center; }
  .info-badge .inner { width: 60px; height: 60px; border-radius: 50%; display: flex; align-items: center; justify-content: center; }
  .info-badge .core { width: 36px; height: 36px; border-radius: 50%; background: var(--white); display: flex; align-items: center; justify-content: center; }
  .info-label { position: absolute; font-size: 14px; color: var(--ink); }
  .info-value { position: absolute; font-size: 18px; font-weight: 700; color: var(--ink); }

  /* form */
  .form-panel { position: absolute; left: 461px; top: 552px; width: 473px; height: 380px; background: var(--navy);
    border-radius: 0 84px 0 77px; }
  .field { position: absolute; background: var(--white); font-size: 11px; color: var(--field-text); padding: 0 13px; line-height: 35px; height: 35px; width: 195px; }
  .field.message { height: 98px; width: 399px; line-height: 1; padding-top: 13px; }
  .submit { position: absolute; left: 496px; top: 851px; width: 139px; height: 39px; border-radius: 20px; background: var(--orange);
    color: var(--white); font-family: "Montserrat", sans-serif; font-weight: 700; font-size: 12px; display: flex; align-items: center; justify-content: center; }

  /* footer */
  .site-footer { position: absolute; left: 0; top: 1032px; width: 1002px; height: 168px; background: var(--ink); color: var(--white); }
  .site-footer .brand { left: 112px; top: 26px; font-size: 28px; color: var(--white); line-height: 40px; }
  .site-footer .brand-dot { background: var(--white); }
  .footer-nav a { position: absolute; top: 39px; font-size: 12px; color: var(--white); text-decoration: none; }
  .site-footer .call { left: 777px; top: 31px; font-size: 14px; font-weight: 700; color: var(--white); }
  .footer-rule { position: absolute; left: 111px; top: 98px; width: 827px; height: 1px; background: #4a3b6a; }
  .copyright { position: absolute; left: 121px; top: 122px; font-size: 10px; color: #d9d4e6; }
  .social { position: absolute; top: 118px; width: 21px; height: 21px; border-radius: 50%; background: var(--white); }
</style>
</head>
<body>

<header class="site-header">
  <div class="brand"><span class="brand-dot"></span>QuillRests</div>
  <nav class="main-nav">
    <a href="#" style="left:393px">How it Works</a>
    <a href="#" style="left:538px">Resources</a>
    <a href="#" class="active" style="left:668px">Contact</a>
  </nav>
  <div class="call">
    <span class="call-icon"><svg width="13" height="13" viewBox="0 0 24 24"><path fill="#fff" d="M6.6 10.8a15.1 15.1 0 0 0 6.6 6.6l2.2-2.2c.3-.3.7-.4 1-.2 1.1.4 2.3.6 3.6.6.6 0 1 .4 1 1V20c0 .6-.4 1-1 1A17 17 0 0 1 3 4c0-.6.4-1 1-1h3.5c.6 0 1 .4 1 1 0 1.3.2 2.5.6 3.6.1.3 0 .7-.2 1z"/></svg></span>
    555-014-2287
  </div>
</header>

<section class="hero">
  <svg class="hero-art" width="1002" height="411" viewBox="0 0 1002 411">
    <defs>
      <linearGradient id="photoTone" x1="0" y1="0" x2="1" y2="1">
        <stop offset="0" stop-color="#cfe8ee"/>
        <stop offset="0.5" stop-color="#8fc3cf"/>
        <stop offset="1" stop-color="#e4eef2"/>
      </linearGradient>
    </defs>
    <ellipse cx="700" cy="245" rx="232" ry="112" transform="rotate(-22 700 245)" fill="none" stroke="#b9b3dc" stroke-width="1" opacity="0.7"/>
    <ellipse cx="700" cy="245" rx="212" ry="98" transform="rotate(-22 700 245)" fill="none" stroke="#b9b3dc" stroke-width="1" opacity="0.6"/>
    <circle cx="702" cy="199" r="177" fill="var(--orange)"/>
    <circle cx="708" cy="201" r="172" fill="url(#photoTone)" role="img" aria-label="Photo of a clinician in a white coat holding a tablet"/>
  </svg>
  <p class="hero-kicker">Get in touch with us</p>
  <h1 class="hero-title">Contact Us</h1>
</section>

<h2 class="contact-heading"><span class="light">Contact</span><span class="bold">QuillRests</span></h2>
<div class="heading-rule"></div>
<p class="intro">Lorem ipsum dolor sit amet, consectetur adipiscing elit, sed do eiusmod tempor incididunt.</p>

<div class="info-badge" style="left:100px;top:739px">
  <div class="inner" style="background:#3b2668">
    <div class="core"><svg width="18" height="18" viewBox="0 0 24 24"><path fill="#3b2668" d="M6.6 10.8a15.1 15.1 0 0 0 6.6 6.6l2.2-2.2c.3-.3.7-.4 1-.2 1.1.4 2.3.6 3.6.6.6 0 1 .4 1 1V20c0 .6-.4 1-1 1A17 17 0 0 1 3 4c0-.6.4-1 1-1h3.5c.6 0 1 .4 1 1 0 1.3.2 2.5.6 3.6.1.3 0 .7-.2 1z"/></svg></div>
  </div>
</div>
<p class="info-label" style="left:188px;top:746px">Phone Number</p>
<p class="info-value" style="left:187px;top:767px">555-014-2287</p>

<div class="info-badge" style="left:100px;top:821px">
  <div class="inner" style="background:var(--navy)">
    <div class="core"><svg width="20" height="14" viewBox="0 0 20 14"><rect x="1" y="1" width="18" height="12" fill="none" stroke="#3d4c98" stroke-width="1.6"/><path d="M1 1l9 7 9-7M1 13l7-6M19 13l-7-6" fill="none" stroke="#3d4c98" stroke-width="1.4"/></svg></div>
  </div>
</div>
<p class="info-label" style="left:187px;top:835px">Email address</p>
<p class="info-value" style="left:187px;top:857px;font-size:15px">hello@quillrests.com</p>

<form class="form-panel-wrap">
  <div class="form-panel"></div>
  <div class="field" style="left:496px;top:605px">First Name</div>
  <div class="field" style="left:701px;top:605px">Last Name</div>
  <div class="field" style="left:496px;top:650px">Email address</div>
  <div class="field" style="left:701px;top:650px">Phone number</div>
  <div class="field" style="left:497px;top:696px">Subject</div>
  <div class="field" style="left:701px;top:696px">Address</div>
  <div class="field message" style="left:498px;top:742px">Message</div>
  <div class="submit">Submit Now</div>
</form>

<footer class="site-footer">
  <div class="brand"><span class="brand-dot"></span>QuillRests</div>
  <nav class="footer-nav">
    <a href="#" style="left:389px">HOME</a>
    <a href="#" style="left:459px">HOW IT WORKS</a>
    <a href="#" style="left:580px">RESOURCES</a>
    <a href="#" style="left:682px">CONTACT</a>
  </nav>
  <div class="call">
    <span class="call-icon" style="width:28px;height:28px"><svg width="14" height="14" viewBox="0 0 24 24"><path fill="#fff" d="M6.6 10.8a15.1 15.1 0 0 0 6.6 6.6l2.2-2.2c.3-.3.7-.4 1-.2 1.1.4 2.3.6 3.6.6.6 0 1 .4 1 1V20c0 .6-.4 1-1 1A17 17 0 0 1 3 4c0-.6.4-1 1-1h3.5c.6 0 1 .4 1 1 0 1.3.2 2.5.6 3.6.1.3 0 .7-.2 1z"/></svg></span>
    555-014-2287
  </div>
  <div class="footer-rule"></div>
  <p class="copyright">©2022 by QuillRests LLC. All Right Reserved</p>
  <span class="social" style="left:842px"></span>
  <span class="social" style="left:867px"></span>
  <span class="social" style="left:892px"></span>
</footer>

</body>
</html>
```